Fiber Arts Workshop: Business Cards & Stationery
Copper Kettle StitchHouse, LLC
Fiber Arts Workshop: Business Cards & Stationery - Hobbies
Creative Brief
Bright & Fun-filled
Marla Penrose
Principal
48 Birchwood Terrace #512 Millbrook, New Jersey 07322
marla.penrose@ckstitchhouse.example
www.ckstitchhouse.example
Fonts - you may use fonts other than those used in the logo if they enhance the design

```html
<!DOCTYPE html>
<html lang="en">
<head>
<meta charset="utf-8">
<title>Copper Kettle StitchHouse, LLC — Stationery Set</title>
<link href="https://fonts.googleapis.com/css2?family=Quicksand:wght@500;700&family=Open+Sans:wght@400;600&display=swap" rel="stylesheet">
<style>
  :root {
    --backdrop: #4b3527;
    --paper: #ffffff;
    --plum: #8e2a7e;
    --plum-soft: #b45aa5;
    --tangerine: #ea6a2a;
    --ink: #4a4a4a;
    --ink-soft: #8a8a8a;
    --seal: #2b2326;
  }
  * { box-sizing: border-box; margin: 0; padding: 0; }
  html, body { width: 1200px; height: 466px; overflow: hidden; }
  body {
    background: var(--backdrop);
    position: relative;
    font-family: "Open Sans", sans-serif;
    color: var(--ink);
  }
  .brand {
    display: flex; align-items: center; gap: 4px;
    font-family: "Quicksand", sans-serif; font-weight: 700;
    color: var(--plum); line-height: 1.05;
  }
  .brand-dot { border-radius: 50%; background: var(--plum); flex: none; }

  /* business cards */
  .business-card {
    position: absolute; left: 8px; width: 72px; height: 32px;
    background: var(--paper); padding: 4px 5px;
  }
  .business-card--plum { top: 240px; border-bottom: 3px solid var(--plum); }
  .business-card--tangerine { top: 282px; border-bottom: 3px solid var(--tangerine); }
  .business-card .brand { font-size: 4.5px; }
  .business-card .brand-dot { width: 6px; height: 6px; }
  .business-card .card-lines { margin-top: 4px; font-size: 2.6px; color: var(--ink-soft); line-height: 1.3; }

  /* letterheads */
  .letterhead {
    position: absolute; top: 29px; width: 276px; height: 421px;
    background: var(--paper); padding: 18px 22px;
  }
  .letterhead--plum { left: 96px; border: 4px solid var(--plum); }
  .letterhead--tangerine { left: 384px; border: 7px solid var(--tangerine); }
  .letter-header { display: flex; justify-content: space-between; align-items: flex-start; }
  .letterhead .brand { font-size: 7px; width: 70px; }
  .letterhead .brand-dot { width: 12px; height: 12px; }
  .letter-contact { font-size: 4px; text-align: right; line-height: 1.35; color: var(--ink-soft); }
  .letter-body { margin-top: 26px; font-size: 5px; line-height: 1.7; color: var(--ink); }
  .letter-body p { margin-bottom: 7px; }
  .letter-date { text-align: right; margin-bottom: 10px; }
  .letter-sign { margin-top: 10px; }
  .letter-sign strong { display: block; font-weight: 600; color: var(--plum); }
  .letter-mark {
    position: absolute; left: 60px; top: 230px; width: 150px; height: 90px; border-radius: 50%;
    background: radial-gradient(closest-side, rgba(180,90,165,.10), rgba(234,106,42,.05), transparent);
  }
  .letter-footer {
    position: absolute; left: 22px; right: 22px; bottom: 14px;
    font-size: 4px; color: var(--ink-soft); text-align: center;
    border-top: 1px solid var(--plum-soft); padding-top: 4px;
  }
  .letterhead--tangerine .letter-footer { border-top-color: var(--tangerine); }

  /* envelopes */
  .envelope { position: absolute; left: 720px; width: 446px; }
  .envelope svg { display: block; }
  .envelope--back-plum { top: 29px; }
  .envelope--back-tangerine { top: 170px; }
  .envelope--front { top: 250px; height: 112px; background: var(--paper); border-bottom: 4px solid var(--tangerine); padding: 12px 16px; }
  .envelope--front .brand { font-size: 7px; width: 80px; }
  .envelope--front .brand-dot { width: 12px; height: 12px; }
  .envelope-return { margin-top: 5px; font-size: 4px; color: var(--ink-soft); line-height: 1.4; }
</style>
</head>
<body>

  <div class="business-card business-card--plum">
    <div class="brand"><span class="brand-dot"></span>Copper Kettle<br>StitchHouse, LLC</div>
    <div class="card-lines">Marla Penrose · Principal<br>www.ckstitchhouse.example</div>
  </div>
  <div class="business-card business-card--tangerine">
    <div class="brand"><span class="brand-dot"></span>Copper Kettle<br>StitchHouse, LLC</div>
    <div class="card-lines">marla.penrose@ckstitchhouse.example<br>48 Birchwood Terrace #512</div>
  </div>

  <section class="letterhead letterhead--plum">
    <div class="letter-header">
      <div class="brand"><span class="brand-dot"></span>Copper Kettle StitchHouse, LLC</div>
      <div class="letter-contact">48 Birchwood Terrace #512<br>Millbrook, New Jersey 07322<br>www.ckstitchhouse.example</div>
    </div>
    <div class="letter-mark" role="img" aria-label="Faint brand colour wash"></div>
    <div class="letter-body">
      <p class="letter-date">March 4, 2024</p>
      <p>Dear Friend,</p>
      <p>Thank you for visiting our studio this season. We are delighted to share new classes in knitting, spinning and weaving for every skill level.</p>
      <p>Our members enjoy open stitch nights, yarn swaps and friendly guidance from teachers who love the craft as much as you do.</p>
      <p class="letter-sign">Warm regards,<strong>Marla Penrose</strong>Principal</p>
    </div>
    <div class="letter-footer">48 Birchwood Terrace #512, Millbrook, New Jersey 07322 · marla.penrose@ckstitchhouse.example</div>
  </section>

  <section class="letterhead letterhead--tangerine">
    <div class="letter-header">
      <div class="brand"><span class="brand-dot"></span>Copper Kettle StitchHouse, LLC</div>
      <div class="letter-contact">48 Birchwood Terrace #512<br>Millbrook, New Jersey 07322<br>www.ckstitchhouse.example</div>
    </div>
    <div class="letter-mark" role="img" aria-label="Faint brand colour wash"></div>
    <div class="letter-body">
      <p class="letter-date">March 4, 2024</p>
      <p>Dear Friend,</p>
      <p>Thank you for visiting our studio this season. We are delighted to share new classes in knitting, spinning and weaving for every skill level.</p>
      <p>Our members enjoy open stitch nights, yarn swaps and friendly guidance from teachers who love the craft as much as you do.</p>
      <p class="letter-sign">Warm regards,<strong>Marla Penrose</strong>Principal</p>
    </div>
    <div class="letter-footer">48 Birchwood Terrace #512, Millbrook, New Jersey 07322 · www.ckstitchhouse.example</div>
  </section>

  <div class="envelope envelope--back-plum">
    <svg width="446" height="135" viewBox="0 0 446 135">
      <rect x="0" y="0" width="446" height="135" fill="var(--paper)"/>
      <path d="M0 0 H446 V70 Q223 120 0 70 Z" fill="var(--paper)" stroke="var(--plum)" stroke-width="6"/>
      <path d="M8 8 H438 V62 Q223 108 8 62 Z" fill="none" stroke="var(--plum-soft)" stroke-width="1"/>
      <circle cx="223" cy="86" r="14" fill="var(--seal)"/>
      <circle cx="223" cy="26" r="10" fill="var(--plum)"/>
    </svg>
  </div>

  <div class="envelope envelope--back-tangerine">
    <svg width="446" height="80" viewBox="0 0 446 80">
      <rect x="0" y="0" width="446" height="80" fill="var(--paper)"/>
      <path d="M0 8 H446 V40 Q223 75 0 40 Z" fill="var(--paper)" stroke="var(--tangerine)" stroke-width="6"/>
      <circle cx="223" cy="30" r="8" fill="var(--plum)"/>
    </svg>
  </div>

  <div class="envelope envelope--front">
    <div class="brand"><span class="brand-dot"></span>Copper Kettle StitchHouse, LLC</div>
    <div class="envelope-return">48 Birchwood Terrace #512<br>Millbrook, New Jersey 07322<br>www.ckstitchhouse.example</div>
  </div>

</body>
</html>
```